Banner Ad Design Project

I need a banner design. The website is under construction at www.brightmarrow.example

Name: Bright Marrow
Tagline: Steady Sparks for crowded calendars

This is a leadership development and executive coaching site. The past site is live at www.quillstepnow.example. (so you can get a sense of the content)

The audience are (BUSY) executives, senior managers, leaders and top professionals, so the feel needs to be highly professional but also modern and fresh. I want to communicate energy but also solid and trust worthy and not too new agey. The audience are also people with strong social values who want to change things - so not too corporate (Ie suits!)

I would like the design to be floating on a white background, very clean and simple. I am attracted to reds or sunset (burn orange crimson colors.) But totally open to any color ideas.
I am giving an open brief for your ideas.
Here are the dimensions 960px wide, roughly 190px height.

Reason: The weekend might give more time to designers to get involved. Thanks Vina

Hi designers

You may not have seen the additions I gave to this brief.

The banner should not have leader out front photo's. Maybe less corporate than I initially thought. 
Not too corporate (no suits!) Please no chess pieces, jigsaw pieces, cartoon images, cliche leadership images. 
Am am trying for inspiration /inspiring whilst still being professional. Very simple and clean.
Please can the design be floating in a white background so that the web page is borderless - A bit like it is in http://palmoriskel.example/
Thank you

Target Market(s)

Senior managers, executives but people who also want to change the world!

Industry/Entity Type

Construction

Requirements
Should not have
• Should not have leader out front photo's.
Maybe less corporate than I initially thought.
Am am trying for inspiration /inspiring whilst still being professional.
Please no chess pieces, jigsaw pieces, cartoon images, cliche leadership images. Not too corporate (Ie suits!)

Thanks

```html
<!DOCTYPE html>
<html lang="en">
<head>
<meta charset="utf-8">
<title>Bright Marrow – Banner Options</title>
<link rel="stylesheet" href="https://fonts.googleapis.com/css2?family=Open+Sans:wght@500&display=swap">
<style>
  :root {
    --board: #3a3a3a;
    --paper: #ffffff;
    --peach: #fde3c6;
    --peach-soft: #fff3e6;
    --streak: rgba(248, 190, 140, 0.45);
    --brand-orange: #f06514;
    --ink: #3b2418;
    --globe-light: #cfe3f7;
    --globe-mid: #3a8ae0;
    --globe-deep: #0b4fb8;
  }
  * { box-sizing: border-box; margin: 0; padding: 0; }
  html, body {
    width: 1200px;
    height: 768px;
    overflow: hidden;
    background: var(--board);
  }
  .board {
    position: relative;
    width: 1200px;
    height: 768px;
  }
  .banner {
    position: absolute;
    left: 24px;
    width: 1152px;
    height: 228px;
    overflow: hidden;
    background:
      linear-gradient(172deg, transparent 52%, var(--streak) 60%, transparent 70%),
      linear-gradient(176deg, transparent 58%, rgba(250, 205, 160, 0.35) 64%, transparent 72%),
      linear-gradient(180deg, var(--peach-soft) 0%, var(--paper) 22%, var(--paper) 72%, var(--peach) 100%);
  }
  .banner--one { top: 24px; }
  .banner--two { top: 270px; }
  .banner--three { top: 516px; }
  .brand {
    position: absolute;
    left: 62px;
    top: 58px;
    z-index: 2;
  }
  .brand-name {
    font-family: "Open Sans", Arial, sans-serif;
    font-weight: 500;
    font-size: 54px;
    line-height: 1;
    letter-spacing: 0;
    color: var(--brand-orange);
  }
  .brand-tagline {
    margin-top: 18px;
    font-family: "Open Sans", Arial, sans-serif;
    font-weight: 500;
    font-size: 15.5px;
    letter-spacing: 1.6px;
    text-transform: uppercase;
    color: var(--ink);
  }
  .globe {
    position: absolute;
    inset: 0;
    width: 1152px;
    height: 228px;
    z-index: 1;
  }
</style>
</head>
<body>
<main class="board">

  <section class="banner banner--one">
    <svg class="globe" viewBox="0 0 1152 228" role="img" aria-label="Blue glossy globe showing Europe and Africa">
      <defs>
        <radialGradient id="globe-fill-a" cx="0.4" cy="0.3" r="0.75">
          <stop offset="0" stop-color="var(--globe-light)"/>
          <stop offset="0.45" stop-color="var(--globe-mid)"/>
          <stop offset="1" stop-color="var(--globe-deep)"/>
        </radialGradient>
      </defs>
      <ellipse cx="950" cy="226" rx="100" ry="8" fill="rgba(0,0,0,0.12)"/>
      <circle cx="948" cy="118" r="108" fill="url(#globe-fill-a)"/>
    </svg>
    <div class="brand">
      <h1 class="brand-name">Bright Marrow</h1>
      <p class="brand-tagline">Steady Sparks for crowded calendars</p>
    </div>
  </section>

  <section class="banner banner--two">
    <svg class="globe" viewBox="0 0 1152 228" role="img" aria-label="Large blue globe rising from the bottom edge, showing northern Europe">
      <defs>
        <radialGradient id="globe-fill-b" cx="0.45" cy="0.35" r="0.7">
          <stop offset="0" stop-color="var(--globe-light)"/>
          <stop offset="0.5" stop-color="var(--globe-mid)"/>
          <stop offset="1" stop-color="var(--globe-deep)"/>
        </radialGradient>
      </defs>
      <circle cx="886" cy="228" r="224" fill="url(#globe-fill-b)"/>
    </svg>
    <div class="brand">
      <h1 class="brand-name">Bright Marrow</h1>
      <p class="brand-tagline">Steady Sparks for crowded calendars</p>
    </div>
  </section>

  <section class="banner banner--three">
    <div class="brand">
      <h1 class="brand-name">Bright Marrow</h1>
      <p class="brand-tagline">Steady Sparks for crowded calendars</p>
    </div>
  </section>

</main>
</body>
</html>
```